Website Design for PawRank - New Digital Agency

We are creating a new digital marketing agency and need a new website. I have attached the logo. Our niche is going to be veterinarians. Use the same colors as in the logo (blue, white and gray).

I want real pictures of real people in this and not just boring stock photos. It needs to be related to the industry.

Home page (example:https://trellmarsh.com/)
Service page (example: https://dovequist.com/consulting/)
Case study page (example: https://www.harlowfinchley.com/seo/case-study/)

I will continue to update this brief.
Updates

I updated the brief with some additional sample sites 2 days ago and want to see more designs. I won't need that may more days ...just a few more.

Target Market(s)

veterinarians

Font styles to use
Sans Serif

Requirements
Must have
• I want a very clean looking site. Use the same colors as in the logo (blue, white and gray).
Nice to have
• We need to build this with the idea that the purpose is to generate leads for our business.
• Home page (example:https://trellmarsh.com/)
• Service page (example: https://dovequist.com/consulting/)
• Case study page (example: https://www.harlowfinchley.com/seo/case-study/)

```html
<!DOCTYPE html>
<html lang="en">
<head>
<meta charset="utf-8">
<title>PawRank — Digital Marketing for Veterinarians</title>
<link href="https://fonts.googleapis.com/css2?family=Raleway:wght@500;600;700&family=Lato:wght@400;700&display=swap" rel="stylesheet">
<style>
:root{
  --blue:#0f3f94;
  --blue-bright:#1a4fb0;
  --ink:#3d3d3d;
  --text:#6a6a6a;
  --gray-dark:#4a4a4c;
  --gray-bar:#4f4f51;
  --gray-light:#f1f2f4;
  --white:#ffffff;
  --line:#d9dbe0;
}
*{box-sizing:border-box;margin:0;padding:0}
html,body{width:1200px;height:4144px;overflow:hidden;background:var(--white)}
body{font-family:'Lato',sans-serif;color:var(--text)}
.page{position:relative;width:1200px;height:4144px;overflow:hidden}
.abs{position:absolute}
h1,h2,h3,.heading{font-family:'Raleway',sans-serif;color:var(--ink)}

/* top bar */
.topbar{left:0;top:0;width:1200px;height:40px;background:var(--gray-bar);color:#e5e5e5;font-size:11px;display:flex;align-items:center}
.topbar .contact{position:absolute;left:174px;display:flex;gap:38px;align-items:center}
.topbar .contact span{display:flex;align-items:center;gap:6px}
.topbar .social{position:absolute;right:180px;display:flex;gap:22px}
.topbar .social i{display:block;width:11px;height:11px;border:1.5px solid #e5e5e5;border-radius:50%}

/* nav */
.nav{left:0;top:40px;width:1200px;height:92px;background:var(--white);border-bottom:1px solid #eee}
.brand{position:absolute;left:174px;top:26px;display:flex;align-items:center;gap:10px;font-family:'Raleway',sans-serif;font-weight:700;font-size:34px;color:var(--blue)}
.brand .dot{width:14px;height:14px;border-radius:50%;background:var(--blue)}
.menu{position:absolute;top:36px;right:173px;display:flex;gap:40px;font-family:'Raleway',sans-serif;font-size:15px;font-weight:500;color:var(--ink)}
.menu a{white-space:nowrap;color:inherit;text-decoration:none}
.menu a.active{color:var(--blue-bright)}

/* hero */
.hero-art{left:0;top:0;width:1200px;height:830px}
.hero-copy{left:172px;top:318px}
.hero-copy h1{font-size:64px;font-weight:700;color:var(--ink);line-height:1;letter-spacing:-1px}
.hero-copy h1 .accent{color:var(--blue)}
.hero-copy p{margin-top:26px;font-size:20px;line-height:31px;color:#444;width:320px}
.btn{display:inline-block;background:var(--blue);color:var(--white);font-family:'Raleway',sans-serif;font-weight:600;font-size:13px;padding:0;width:118px;height:40px;line-height:40px;text-align:center}
.hero-copy .btn{margin-top:32px}

/* welcome */
.welcome{left:172px;top:920px;width:434px}
.welcome h2{font-size:31px;font-weight:600}
.welcome p{margin-top:26px;font-size:11px;line-height:23.3px;text-align:justify}
.welcome .btn{margin-top:24px}
.portrait{left:656px;top:870px}

/* why */
.why-photo{left:0;top:1361px;width:600px;height:565px;background:linear-gradient(120deg,#c9bfae 0%,#8d8576 40%,#53534f 70%,#9a9585 100%)}
.why-panel{left:600px;top:1361px;width:600px;height:565px;background:var(--blue);color:#e4ebf7;padding:98px 0 0 47px}
.why-panel h2{color:var(--white);font-size:30px;font-weight:600}
.why-panel .lead{margin-top:18px;width:370px;font-size:11px;line-height:21px}
.why-panel ul{list-style:none;margin-top:22px}
.why-panel li{display:flex;align-items:center;gap:9px;font-size:11px;height:25.6px}

/* services */
.section-head{left:0;width:1200px;text-align:center}
.section-head h2{font-size:31px;font-weight:600}
.section-head p{margin:18px auto 0;width:500px;font-size:11px;line-height:24px}
.service{width:300px;height:110px}
.service .icon{position:absolute;left:0;top:0;width:100px;height:100px;border-radius:50%;background:var(--blue);display:flex;align-items:center;justify-content:center}
.service h3{position:absolute;left:116px;top:0;font-size:18px;font-weight:500;color:#333;white-space:nowrap}
.service p{position:absolute;left:116px;top:34px;width:270px;font-size:10.5px;line-height:19px}

/* news */
.news-bg{left:0;top:2662px;width:1200px;height:1200px;background:linear-gradient(180deg,#e7e9ec 0%,#f4f5f7 35%,#eef0f2 100%)}
.card{top:2895px;width:260px;height:370px;background:var(--white);box-shadow:0 2px 10px rgba(0,0,0,.08)}
.card .img{height:174px}
.card .date{position:absolute;left:21px;top:199px;width:44px;height:44px;border-radius:50%;background:var(--blue);color:var(--white);text-align:center;font-family:'Raleway',sans-serif}
.card .date b{display:block;font-size:17px;line-height:20px;margin-top:6px}
.card .date small{display:block;font-size:9px;line-height:10px}
.card h3{position:absolute;left:77px;top:200px;font-size:16px;font-weight:600;line-height:20px;color:#333}
.card p{position:absolute;left:21px;top:262px;width:225px;font-size:10.5px;line-height:18px}
.card a{position:absolute;left:21px;top:332px;font-family:'Raleway',sans-serif;font-weight:700;font-size:10.5px;color:var(--ink);text-decoration:underline}
.divider{left:174px;top:3373px;width:852px;height:1px;background:var(--line)}

/* testimonial */
.avatar{left:196px;top:3452px;width:122px;height:122px;border-radius:50%;border:3px solid var(--white);background:linear-gradient(135deg,#dfe3e8,#a9b3bf);box-shadow:0 0 0 1px #ccc}
.quote-badge{left:179px;top:3444px;width:54px;height:54px;border-radius:50%;background:var(--blue);color:var(--white);font-family:'Raleway',sans-serif;font-weight:700;font-size:34px;line-height:64px;text-align:center}
.testimonial{left:347px;top:3452px;width:580px}
.testimonial p{font-style:italic;font-size:11px;line-height:22px;color:#555}
.testimonial .who{margin-top:24px;font-family:'Raleway',sans-serif;font-size:16px;color:var(--ink)}
.testimonial .who b{color:var(--blue-bright);font-weight:600}
.arrows{left:995px;top:3476px}

/* footer */
.footer-shape{left:0;top:3560px;width:1200px;height:584px}
.footer-brand{left:740px;top:3716px;font-family:'Raleway',sans-serif;font-weight:700;font-size:62px;color:var(--white);display:flex;align-items:center;gap:14px}
.footer-brand .dot{width:22px;height:22px;border-radius:50%;background:var(--white)}
.fcol{top:3850px;color:#e2e2e2;font-size:11px}
.fcol h4{font-family:'Raleway',sans-serif;font-size:14px;font-weight:700;color:var(--white);margin-bottom:16px}
.fcol li{list-style:none;line-height:22.5px}
.fcontact .row{display:flex;gap:16px;line-height:19px;margin-bottom:16px}
.copyright{left:0;top:4080px;width:1200px;text-align:center;color:#e2e2e2;font-size:12px}
</style>
</head>
<body>
<div class="page">

  <svg class="abs hero-art" viewBox="0 0 1200 830" role="img" aria-label="Photo of a smiling veterinarian with a stethoscope hugging a yellow labrador in a bright clinic">
    <defs>
      <linearGradient id="heroTone" x1="0" y1="0" x2="1" y2="0.4">
        <stop offset="0" stop-color="#eef1f4"/>
        <stop offset="0.45" stop-color="#e6e6e4"/>
        <stop offset="0.7" stop-color="#d9c7a2"/>
        <stop offset="1" stop-color="#b8bcc2"/>
      </linearGradient>
    </defs>
    <polygon points="0,132 1200,132 1200,552 246,785 0,680" fill="url(#heroTone)"/>
    <polygon points="0,680 246,785 965,613 246,808 0,697" fill="#0f3f94"/>
  </svg>

  <header>
    <div class="abs topbar">
      <div class="contact">
        <span><svg width="11" height="8" viewBox="0 0 11 8"><rect x=".5" y=".5" width="10" height="7" fill="none" stroke="#e5e5e5"/><path d="M.5 .5 5.5 4.5 10.5 .5" fill="none" stroke="#e5e5e5"/></svg>Email: hello@pawrank.com</span>
        <span><svg width="10" height="10" viewBox="0 0 10 10"><path d="M2 1 4 3 3 4.3C3.8 5.8 4.5 6.5 5.8 7L7 6 9 8 7.6 9.3C4 9 1 6 .7 2.4Z" fill="#e5e5e5"/></svg>Phone: 1-800-555-0142</span>
      </div>
      <div class="social"><i></i><i></i><i></i><i></i></div>
    </div>
    <nav class="abs nav">
      <div class="brand">PawRank<span class="dot"></span></div>
      <div class="menu">
        <a class="active">Home</a>
        <a>About PawRank</a>
        <a>What We Do</a>
        <a>News</a>
        <a>Team</a>
        <a>Contact</a>
      </div>
    </nav>
  </header>

  <section class="abs hero-copy">
    <h1>Paw<span class="accent">Rank</span></h1>
    <p>Sed ut perspiciatis unde omnis iste natus&nbsp; sit voluptatem accusan.</p>
    <a class="btn">Read More</a>
  </section>

  <section class="abs welcome">
    <h2>Welcome to PawRank</h2>
    <p>Sed ut perspiciatis unde omnis iste natus error sit voluptatem accusantium doloremque laudantium, totam rem aperiam, eaque ipsa quae ab illo inventore veritatis et quasi architecto beatae vitae dicta sunt explicabo. Nemo enim ipsam voluptatem quia voluptas sit aspernatur aut odit aut fugit, sed quia consequuntur magni dolores eos qui ratione voluptatem sequi nesciunt. Neque porro quisquam est, qui dolorem ipsum quia dolor sit amet, consectetur, adipisci velit, sed quia non numquam eius modi tempora incidunt ut labore et dolore magnSed ut perspiciatis unde omnis iste natus error sit voluptatem accusantium doloremque laudantium, totam rem aperiam, eaque ipsa quae ab illo inventore veritatis et quasi architecto beatae vitae dicta sunt explicabo.</p>
    <a class="btn">Read More</a>
  </section>
  <svg class="abs portrait" width="400" height="400" viewBox="0 0 400 400" role="img" aria-label="Round photo of a veterinarian in a yellow sweater examining a small animal on a clinic table">
    <defs>
      <linearGradient id="portraitTone" x1="0" y1="0" x2="1" y2="1">
        <stop offset="0" stop-color="#c7c3b8"/>
        <stop offset="0.5" stop-color="#d9a93a"/>
        <stop offset="1" stop-color="#8f8a80"/>
      </linearGradient>
    </defs>
    <circle cx="200" cy="196" r="196" fill="#0f3f94"/>
    <circle cx="202" cy="200" r="186" fill="#ffffff"/>
    <circle cx="200" cy="196" r="180" fill="url(#portraitTone)"/>
  </svg>

  <div class="abs why-photo" role="img" aria-label="Photo of two colleagues working together on a laptop at a wooden table"></div>
  <section class="abs why-panel">
    <h2>Why Choose PawRank?</h2>
    <p class="lead">Sed ut perspiciatis unde omnis iste natuserror sit voluptatem accusantium dolorue laudantium, totam rem aperiam, eaque isa quae ab illo inventore veritatis et quasi arc hitecto beatae vitae dictunt ebasi ao beatae vit.</p>
    <ul>
      <li><svg width="14" height="13" viewBox="0 0 14 13"><g fill="#fff"><ellipse cx="7" cy="9" rx="3.6" ry="3"/><circle cx="2" cy="5.5" r="1.6"/><circle cx="5" cy="2" r="1.6"/><circle cx="9" cy="2" r="1.6"/><circle cx="12" cy="5.5" r="1.6"/></g></svg>Lorem ipsum dolor sit amet, consectetur adipiscing elit.</li>
      <li><svg width="14" height="13" viewBox="0 0 14 13"><g fill="#fff"><ellipse cx="7" cy="9" rx="3.6" ry="3"/><circle cx="2" cy="5.5" r="1.6"/><circle cx="5" cy="2" r="1.6"/><circle cx="9" cy="2" r="1.6"/><circle cx="12" cy="5.5" r="1.6"/></g></svg>Phasellus consectetur dui dignissim, cursus arcu sed, cursus arcu.</li>
      <li><svg width="14" height="13" viewBox="0 0 14 13"><g fill="#fff"><ellipse cx="7" cy="9" rx="3.6" ry="3"/><circle cx="2" cy="5.5" r="1.6"/><circle cx="5" cy="2" r="1.6"/><circle cx="9" cy="2" r="1.6"/><circle cx="12" cy="5.5" r="1.6"/></g></svg>Nunc ornare sapien quis nisl tristique, et fringilla orci tempor.</li>
      <li><svg width="14" height="13" viewBox="0 0 14 13"><g fill="#fff"><ellipse cx="7" cy="9" rx="3.6" ry="3"/><circle cx="2" cy="5.5" r="1.6"/><circle cx="5" cy="2" r="1.6"/><circle cx="9" cy="2" r="1.6"/><circle cx="12" cy="5.5" r="1.6"/></g></svg>Duis dictum tellus sit amet luctus auctor.</li>
      <li><svg width="14" height="13" viewBox="0 0 14 13"><g fill="#fff"><ellipse cx="7" cy="9" rx="3.6" ry="3"/><circle cx="2" cy="5.5" r="1.6"/><circle cx="5" cy="2" r="1.6"/><circle cx="9" cy="2" r="1.6"/><circle cx="12" cy="5.5" r="1.6"/></g></svg>Maecenas gravida eros porttitor pretium volutpat.</li>
      <li><svg width="14" height="13" viewBox="0 0 14 13"><g fill="#fff"><ellipse cx="7" cy="9" rx="3.6" ry="3"/><circle cx="2" cy="5.5" r="1.6"/><circle cx="5" cy="2" r="1.6"/><circle cx="9" cy="2" r="1.6"/><circle cx="12" cy="5.5" r="1.6"/></g></svg>Fusce vitae mi ornare, volutpat nulla sed, malesuada orci.</li>
      <li><svg width="14" height="13" viewBox="0 0 14 13"><g fill="#fff"><ellipse cx="7" cy="9" rx="3.6" ry="3"/><circle cx="2" cy="5.5" r="1.6"/><circle cx="5" cy="2" r="1.6"/><circle cx="9" cy="2" r="1.6"/><circle cx="12" cy="5.5" r="1.6"/></g></svg>Ut auctor est sit amet metus ornare, vel bibendum metus sagittis.</li>
      <li><svg width="14" height="13" viewBox="0 0 14 13"><g fill="#fff"><ellipse cx="7" cy="9" rx="3.6" ry="3"/><circle cx="2" cy="5.5" r="1.6"/><circle cx="5" cy="2" r="1.6"/><circle cx="9" cy="2" r="1.6"/><circle cx="12" cy="5.5" r="1.6"/></g></svg>Pellentesque ut justo quis risus cursus gravida eget sit amet justo.</li>
      <li><svg width="14" height="13" viewBox="0 0 14 13"><g fill="#fff"><ellipse cx="7" cy="9" rx="3.6" ry="3"/><circle cx="2" cy="5.5" r="1.6"/><circle cx="5" cy="2" r="1.6"/><circle cx="9" cy="2" r="1.6"/><circle cx="12" cy="5.5" r="1.6"/></g></svg>Vivamus molestie felis at dolor ultricies sollicitudin.</li>
    </ul>
  </section>

  <div class="abs section-head" style="top:2036px">
    <h2>What We Do</h2>
    <p>Sed ut perspiciatis unde omnis iste natus error sit voluptatem accusantium doloremque laudantium, totam rem aperiam, eaque ipsa quae ab illo inventore veritatis et quasi architecto beatae vitae.</p>
  </div>

  <div class="abs service" style="left:172px;top:2180px">
    <div class="icon"><svg width="54" height="54" viewBox="0 0 54 54" fill="none" stroke="#fff" stroke-width="2.5"><circle cx="22" cy="22" r="14"/><circle cx="22" cy="22" r="8"/><path d="M32 32 47 47" stroke-width="5" stroke-linecap="round"/></svg></div>
    <h3>Phasellus consectetdinm</h3>
    <p>Sed ut perspiciatis unde omnis iste natus error siatem accusantium doloremque laudantium, totam reemaue ipsa quae ab illo inventore veritatis et quasrccus.</p>
  </div>
  <div class="abs service" style="left:640px;top:2180px">
    <div class="icon"><svg width="54" height="54" viewBox="0 0 54 54" fill="none" stroke="#fff" stroke-width="2.5"><circle cx="27" cy="18" r="10"/><path d="M9 48V42C9 35 16 31 27 31S45 35 45 42V48Z"/><path d="M21 31V38M33 31V38"/><circle cx="21" cy="41" r="2.5"/><circle cx="33" cy="41" r="2.5"/></svg></div>
    <h3>Phasellus consectetdinm</h3>
    <p>Sed ut perspiciatis unde omnis iste natus error siatem accusantium doloremque laudantium, totam reemaue ipsa quae ab illo inventore veritatis et quasrccus.</p>
  </div>
  <div class="abs service" style="left:172px;top:2315px">
    <div class="icon"><svg width="54" height="54" viewBox="0 0 54 54" fill="none" stroke="#fff" stroke-width="2.5" stroke-linejoin="round"><path d="M8 22H16L36 10V42L16 30H8Z"/><path d="M14 30 18 44H24L21 30"/><path d="M42 18 48 14M43 26H50M42 34 48 38"/><path d="M6 48H30"/></svg></div>
    <h3>Phasellus consectetdinm</h3>
    <p>Sed ut perspiciatis unde omnis iste natus error siatem accusantium doloremque laudantium, totam reemaue ipsa quae ab illo inventore veritatis et quasrccus.</p>
  </div>
  <div class="abs service" style="left:640px;top:2315px">
    <div class="icon"><svg width="54" height="54" viewBox="0 0 54 54" fill="none" stroke="#fff" stroke-width="2.5"><rect x="12" y="9" width="30" height="39" rx="2"/><rect x="20" y="5" width="14" height="8" rx="1"/><path d="M24 20H30V25H35V31H30V36H24V31H19V25H24Z"/><path d="M18 42H36"/></svg></div>
    <h3>Phasellus consectetdinm</h3>
    <p>Sed ut perspiciatis unde omnis iste natus error siatem accusantium doloremque laudantium, totam reemaue ipsa quae ab illo inventore veritatis et quasrccus.</p>
  </div>
  <div class="abs service" style="left:172px;top:2444px">
    <div class="icon"><svg width="54" height="54" viewBox="0 0 54 54" fill="none" stroke="#fff" stroke-width="2.5" stroke-linejoin="round"><path d="M27 46 9 28C3 22 5 12 13 10 19 8 24 12 27 16 30 12 35 8 41 10 49 12 51 22 45 28Z"/><path d="M17 28 25 20 31 24 37 20"/></svg></div>
    <h3>Phasellus consectetdinm</h3>
    <p>Sed ut perspiciatis unde omnis iste natus error siatem accusantium doloremque laudantium, totam reemaue ipsa quae ab illo inventore veritatis et quasrccus.</p>
  </div>
  <div class="abs service" style="left:640px;top:2444px">
    <div class="icon"><svg width="54" height="54" viewBox="0 0 54 54" fill="none" stroke="#fff" stroke-width="2.5"><path d="M27 30C20 30 14 38 16 44 18 48 24 46 27 46S36 48 38 44C40 38 34 30 27 30Z"/><ellipse cx="11" cy="24" rx="4.5" ry="6"/><ellipse cx="20" cy="13" rx="4.5" ry="6"/><ellipse cx="34" cy="13" rx="4.5" ry="6"/><ellipse cx="43" cy="24" rx="4.5" ry="6"/></svg></div>
    <h3>Phasellus consectetdinm</h3>
    <p>Sed ut perspiciatis unde omnis iste natus error siatem accusantium doloremque laudantium, totam reemaue ipsa quae ab illo inventore veritatis et quasrccus.</p>
  </div>

  <div class="abs news-bg" role="img" aria-label="Faded background photo of a veterinarian caring for a pet"></div>
  <div class="abs section-head" style="top:2765px">
    <h2>Latest News</h2>
    <p>Sed ut perspiciatis unde omnis iste natus error sit voluptatem accusantium doloremque laudantium, totam rem aperiam, eaque ipsa quae ab illo inventore veritatis et quasi architecto beatae vitae.</p>
  </div>

  <article class="abs card" style="left:174px">
    <div class="img" role="img" aria-label="Photo of a veterinarian examining a dog's ear" style="background:linear-gradient(135deg,#5fa9b8,#b58a5e 60%,#6d5a48)"></div>
    <div class="date"><b>20</b><small>July</small></div>
    <h3>Pellentesque faucib<br>ut accumsanultric</h3>
    <p>At vero eos et accusamus et iusto odioignis simos ducimus qui blanditiis praesen iulorm voluptatum deleniti atque</p>
    <a>READ MORE</a>
  </article>
  <article class="abs card" style="left:470px">
    <div class="img" role="img" aria-label="Photo of a team working at computers in a dark office" style="background:linear-gradient(135deg,#3a3a3c,#5b6a7c 55%,#2c3036)"></div>
    <div class="date"><b>20</b><small>July</small></div>
    <h3>Pellentesque faucib<br>ut accumsanultric</h3>
    <p>At vero eos et accusamus et iusto odioignis simos ducimus qui blanditiis praesen iulorm voluptatum deleniti atque</p>
    <a>READ MORE</a>
  </article>
  <article class="abs card" style="left:766px">
    <div class="img" role="img" aria-label="Photo of a veterinarian holding a small fluffy dog" style="background:linear-gradient(135deg,#4d5a6e,#8fa3c7 50%,#d8d0c4)"></div>
    <div class="date"><b>20</b><small>July</small></div>
    <h3>Pellentesque faucib<br>ut accumsanultric</h3>
    <p>At vero eos et accusamus et iusto odioignis simos ducimus qui blanditiis praesen iulorm voluptatum deleniti atque</p>
    <a>READ MORE</a>
  </article>

  <div class="abs divider"></div>

  <div class="abs avatar" role="img" aria-label="Round photo of a smiling veterinarian holding a puppy"></div>
  <div class="abs quote-badge">&ldquo;</div>
  <blockquote class="abs testimonial">
    <p>"At vero eos et accusamus et iusto odioignis simos ducimioreus qui blanditiis praesen iulorm voluptatum delenitiue dolores et quas molestias excepturi sint occaati cupiditate non provident, similique sunt in culpa qui officia erunt mollt vero eos et accusamus et iusto odioignis simos ducimus qui blanditiis praesen iulorm volupt atum deleniti atquedes et quas molestias excepturi sint occaati cupiditate non provident, similiqe ficia desunt molitiiaa"</p>
    <div class="who"><b>-Maren Holt</b> City Name</div>
  </blockquote>
  <svg class="abs arrows" width="50" height="40" viewBox="0 0 50 40" fill="none" stroke="#1a4fb0" stroke-width="1.6"><path d="M20 4 6 20 20 36"/><path d="M30 4 44 20 30 36"/></svg>

  <footer>
    <svg class="abs footer-shape" viewBox="0 3560 1200 584">
      <polygon points="0,3848 962,3590 1200,3700 1200,4144 0,4144" fill="#0f3f94"/>
      <polygon points="0,3858 962,3618 1200,3734 1200,4144 0,4144" fill="#4a4a4c"/>
    </svg>
    <div class="abs footer-brand">PawRank<span class="dot"></span></div>

    <div class="abs fcol fcontact" style="left:180px">
      <h4>Contact</h4>
      <div class="row"><svg width="16" height="20" viewBox="0 0 16 20" fill="none" stroke="#e2e2e2" stroke-width="1.3"><path d="M8 19C3 12 1 9 1 7A7 7 0 0 1 15 7C15 9 13 12 8 19Z"/><circle cx="8" cy="7" r="2.5"/></svg><span>412 Larchmere Road,<br>Suite 9, Fenwick</span></div>
      <div class="row"><svg width="18" height="18" viewBox="0 0 18 18" fill="none" stroke="#e2e2e2" stroke-width="1.3"><path d="M4 1 7 5 5 7C6 10 8 12 11 13L13 11 17 14 15 17C8 17 1 10 1 3Z"/></svg><span>8 800 555 014 21<br>8 800 555 078 36</span></div>
      <div class="row"><svg width="18" height="14" viewBox="0 0 18 14" fill="none" stroke="#e2e2e2" stroke-width="1.3"><rect x=".7" y=".7" width="16.6" height="12.6"/><path d="M.7 .7 9 8 17.3 .7"/></svg><span>info@example.com<br>founder@example.com</span></div>
    </div>
    <div class="abs fcol" style="left:447px">
      <h4>About PawRank</h4>
      <ul><li>Lorem ipsum dolo</li><li>Consectetur adipiscing elit.</li><li>Fusce eget leo tincid</li><li>Donec consequat</li><li>Praesent elementum</li><li>Jmauris posueret</li></ul>
    </div>
    <div class="abs fcol" style="left:677px">
      <h4>Information</h4>
      <ul><li>Lorem ipsum dolo</li><li>Consectetur adipiscing elit.</li><li>Fusce eec consequat</li><li>Praesent elementum</li><li>Jmauris posueret</li><li>Aenean a ex eu lectu</li></ul>
    </div>
    <div class="abs fcol" style="left:915px">
      <h4>Other Links</h4>
      <ul><li>Lorem ipsum dolo</li><li>Consecteturiscing elit.</li><li>Fusce eget leo tincid</li><li>Donec consequat</li><li>Praesent elementum</li><li>Aenean a ex eu lectu</li></ul>
    </div>
    <div class="abs copyright">Copyright 2019 PawRank. All Rights Reserved</div>
  </footer>

</div>
</body>
</html>
```